Business cards for law firm with global theme

I'd like business cards with contact info for two offices. They should include the colors and font of the new logo design, which is a stylized globe with an "F" in it. The feel should be very modern and professional.

```html
<!DOCTYPE html>
<html lang="en">
<head>
<meta charset="utf-8">
<title>Vantrell Law – Business Cards</title>
<link href="https://fonts.googleapis.com/css2?family=Poppins:wght@400;500;600;700&display=swap" rel="stylesheet">
<style>
  :root {
    --navy: #173f74;
    --navy-deep: #12335f;
    --sky: #2aa7e0;
    --ink: #1b3a6b;
    --rule: #6f7aa3;
    --paper: #ffffff;
    --ghost: #e9eef6;
    --backdrop: #2b2c2f;
  }
  * { box-sizing: border-box; margin: 0; padding: 0; }
  html, body { width: 1200px; height: 900px; overflow: hidden; }
  body {
    background: var(--backdrop);
    font-family: "Poppins", sans-serif;
    display: flex;
    flex-direction: column;
    align-items: center;
    justify-content: center;
    gap: 40px;
  }
  .card {
    width: 630px;
    height: 360px;
    position: relative;
    overflow: hidden;
    box-shadow: 0 10px 30px rgba(0,0,0,.45);
  }

  /* Front */
  .card-front { background: var(--paper); color: var(--ink); }
  .card-front .edge-band {
    position: absolute; left: 0; right: 0; bottom: 0; height: 12px;
    background: var(--navy);
  }
  .ghost-circle {
    position: absolute; right: -30px; top: 130px;
    width: 230px; height: 230px; border-radius: 50%;
    background: var(--ghost);
  }
  .brand {
    position: absolute; left: 230px; top: 34px;
    display: flex; align-items: center; gap: 16px;
  }
  .brand-dot {
    width: 58px; height: 58px; border-radius: 50%; background: var(--sky);
  }
  .brand-name {
    font-weight: 700; font-size: 36px; letter-spacing: 1px;
    color: var(--navy); text-transform: uppercase; white-space: nowrap;
  }
  .brand-rule {
    position: absolute; left: 240px; top: 106px; width: 280px; height: 2px;
    background: var(--sky);
  }
  .office { position: absolute; font-size: 13px; line-height: 1.5; z-index: 1; }
  .office-one { left: 40px; top: 128px; }
  .office-two { left: 330px; bottom: 30px; }
  .office-title {
    font-weight: 600; font-size: 16px; color: var(--navy);
    padding-bottom: 4px; border-bottom: 1px solid var(--rule);
    width: 250px; margin-bottom: 6px;
  }
  .contact-line { display: flex; align-items: center; gap: 8px; }
  .contact-line svg { width: 13px; height: 13px; flex: none; }
  .icon-fill { fill: var(--sky); }

  /* Back */
  .card-back { background: var(--navy); }
  .back-circle {
    position: absolute; right: 30px; top: -20px;
    width: 380px; height: 380px; border-radius: 50%;
    background: rgba(255,255,255,.05);
  }
  .back-brand {
    position: absolute; left: 0; right: 0; top: 150px;
    text-align: center;
    font-weight: 700; font-size: 44px; letter-spacing: 2px;
    color: #dfe6f1; text-transform: uppercase;
  }
  .back-rule {
    position: absolute; left: 165px; width: 300px; top: 214px; height: 2px;
    background: #c8d3e4;
  }
</style>
</head>
<body>

<section class="card card-front" aria-label="Business card front">
  <div class="ghost-circle"></div>
  <div class="brand">
    <span class="brand-dot"></span>
    <span class="brand-name">Vantrell Law</span>
  </div>
  <div class="brand-rule"></div>

  <div class="office office-one">
    <p class="office-title">Office location one</p>
    <p>118 Harbor Street NW</p>
    <p>Suite 210, Lakeview</p>
    <p>MI 40217</p>
    <p class="contact-line">
      <svg viewBox="0 0 16 16"><path class="icon-fill" d="M4 1l3 3-2 2c1 2 3 4 5 5l2-2 3 3-2 3C7 15 1 9 1 3z"/></svg>
      555-014-2730
    </p>
    <p class="contact-line">
      <svg viewBox="0 0 16 16"><path class="icon-fill" d="M4 1h8v4H4zM1 6h14v6h-3v3H4v-3H1zM5 10v4h6v-4z"/></svg>
      555-014-2730
    </p>
    <p class="contact-line">
      <svg viewBox="0 0 16 16"><path class="icon-fill" d="M1 3h14v10H1zM2 4l6 5 6-5v1L8 10 2 5z"/></svg>
      jordan@vantrelllaw.com
    </p>
  </div>

  <div class="office office-two">
    <p class="office-title">Office location two</p>
    <p>118 Harbor Street NW</p>
    <p>Suite 210, Lakeview</p>
    <p>MI 40217</p>
    <p class="contact-line">
      <svg viewBox="0 0 16 16"><path class="icon-fill" d="M4 1l3 3-2 2c1 2 3 4 5 5l2-2 3 3-2 3C7 15 1 9 1 3z"/></svg>
      555-014-2730
    </p>
    <p class="contact-line">
      <svg viewBox="0 0 16 16"><path class="icon-fill" d="M4 1h8v4H4zM1 6h14v6h-3v3H4v-3H1zM5 10v4h6v-4z"/></svg>
      555-014-2730
    </p>
    <p class="contact-line">
      <svg viewBox="0 0 16 16"><path class="icon-fill" d="M1 3h14v10H1zM2 4l6 5 6-5v1L8 10 2 5z"/></svg>
      jordan@vantrelllaw.com
    </p>
  </div>
  <div class="edge-band"></div>
</section>

<section class="card card-back" aria-label="Business card back">
  <div class="back-circle"></div>
  <p class="back-brand">Vantrell Law</p>
  <div class="back-rule"></div>
</section>

</body>
</html>
```